Lumo Stack - Powerpoint Templates

We are a consultancy to help builders to optimize their planning in order to save building costs. For that reason we need templates for teasers and presentations where we offer our services, show our team and their capacities and present workflows, organization charts, price lists etc.

```html
<!DOCTYPE html>
<html lang="en">
<head>
<meta charset="utf-8">
<title>Lumo Stack – Presentation Templates</title>
<link href="https://fonts.googleapis.com/css2?family=Michroma&family=Montserrat:wght@400;500;600;700&display=swap" rel="stylesheet">
<style>
:root{
  --gold:#c2852c;
  --gold-deep:#a86f1f;
  --yellow:#f2c24f;
  --dark:#2f2f33;
  --ink:#3a3a3a;
  --muted:#6b6b6b;
  --line:#e4e4e4;
  --board:#c9c9c9;
  --white:#ffffff;
}
*{box-sizing:border-box;margin:0;padding:0}
html,body{width:1200px;height:3101px;overflow:hidden}
body{background:var(--board);font-family:"Montserrat",sans-serif;color:var(--ink);position:relative}
.hero-stage{position:absolute;left:0;top:0;width:1200px;height:720px;background:linear-gradient(180deg,#dfe1e6 0%,#eceef1 60%,#d9d6d2 100%)}
.hero-stage .slide{left:149px;top:105px;transform:scale(1.6);transform-origin:0 0;box-shadow:0 8px 30px rgba(0,0,0,.18)}
.slide{position:absolute;width:562px;height:316px;background:var(--white);overflow:hidden}
.slide > *{position:absolute}
.shape{left:0;top:0}
.h-display{font-family:"Michroma",sans-serif;font-size:15px;letter-spacing:1.5px;color:var(--dark);text-transform:uppercase;line-height:1.1}
.h-display.light{color:var(--white)}
.h-bar{width:26px;height:3px;background:var(--gold);border-radius:2px}
.title-gold{font-family:"Michroma",sans-serif;font-size:17px;letter-spacing:1.2px;color:var(--gold)}
.title-dark{font-family:"Michroma",sans-serif;font-size:17px;letter-spacing:1.2px;color:var(--dark)}
.body{font-size:6px;line-height:1.35;color:var(--muted)}
.body.c{text-align:center}
.body.r{text-align:right}
.body.w{color:#fff}
.sub-gold{font-size:9px;font-weight:600;color:var(--gold)}
.sub-dark{font-size:9px;font-weight:600;color:var(--dark)}
.sub-yellow{font-size:9px;font-weight:600;color:var(--yellow)}
.c{text-align:center}
.r{text-align:right}
.tiny{font-size:5px;color:var(--ink);letter-spacing:.2px}
.brand{display:flex;align-items:center;gap:6px}
.brand .sq{width:16px;height:16px;background:var(--gold)}
.brand .name{font-size:12px;font-weight:700;color:var(--gold);letter-spacing:1px}
.foot{left:14px;top:286px;width:534px;height:16px;display:flex;align-items:center}
.foot .sq{width:9px;height:9px;background:var(--gold);margin-right:4px}
.foot .name{font-size:7px;font-weight:700;color:var(--gold);letter-spacing:.6px}
.foot .copy{margin-left:auto;font-size:4.5px;color:var(--ink);margin-right:8px}
.foot .pg{width:9px;height:9px;background:var(--gold);color:#fff;font-size:5px;display:flex;align-items:center;justify-content:center;border-radius:1px}
.ticks{list-style:none}
.ticks li{font-size:6.5px;line-height:1.3;color:#fff;padding-left:10px;position:relative;margin-bottom:5px}
.ticks li::before{content:"✓";position:absolute;left:0;top:0;font-size:6.5px}
.dots{list-style:none}
.dots li{font-size:5px;color:var(--muted);line-height:1.3;margin-bottom:3px;padding-left:7px;position:relative}
.dots li::before{content:"";position:absolute;left:0;top:2px;width:3px;height:3px;border-radius:50%;background:var(--gold)}
.contact-row{display:flex;align-items:center;gap:6px;font-size:7px;color:var(--ink);margin-bottom:8px}
.contact-row svg{width:9px;height:9px}
.contact-head{font-size:10px;font-weight:600;color:var(--dark)}
.data-table{border-collapse:collapse;font-size:5.5px;width:504px}
.data-table th{height:22px;color:#fff;font-weight:600;font-size:5.5px}
.data-table th.lead{background:var(--dark);text-align:left;padding-left:6px;width:156px}
.data-table th.col{background:var(--gold);text-align:center}
.data-table td{height:19px;border-bottom:1px solid var(--line);text-align:center;color:var(--ink)}
.data-table td.lead{text-align:left;padding-left:6px;font-weight:600;color:var(--dark)}
.data-table tr:nth-child(even) td{background:#f6f6f6}
.data-table .hl{font-weight:700}
.col-frame{border:1.5px solid var(--yellow);border-radius:4px}
.pct{font-family:"Michroma",sans-serif;font-size:17px}
</style>
</head>
<body>

<section class="hero-stage">
  <div class="slide">
    <svg class="shape" width="562" height="316" viewBox="0 0 562 316">
      <path d="M238,316 C258,220 266,120 292,62 C310,18 338,0 380,0 L562,0 L562,316 Z" fill="var(--gold)"/>
      <path role="img" aria-label="Photo: two business people looking up at a modern glass building" d="M282,316 C296,230 304,150 326,90 C342,44 364,20 404,0 L562,0 L562,316 Z" fill="url(#heroPhoto)"/>
      <defs><linearGradient id="heroPhoto" x1="0" y1="0" x2="1" y2="1"><stop offset="0" stop-color="#9aa3ab"/><stop offset=".55" stop-color="#5f6770"/><stop offset="1" stop-color="#2e3238"/></linearGradient></defs>
    </svg>
    <div class="brand" style="left:34px;top:36px"><span class="sq"></span><span class="name">LUMO STACK</span></div>
    <div class="title-gold" style="left:34px;top:114px">PRESENTATION</div>
    <div class="title-dark" style="left:34px;top:134px">HEADING HERE</div>
    <p class="body" style="left:34px;top:168px;width:190px">Lorem ipsum dolor sit amet, consectetur adipiscing elit. Vivamus eu dui ex. Curabitur dapibus dignissim dui, in molestie metus feugiat sed. Praesent aliquet lorem ex.</p>
    <p class="body" style="left:34px;top:222px;color:var(--ink)">Saturday, July 8, 2023</p>
    <p class="tiny" style="left:34px;top:276px">COPYRIGHT © 2023 LUMO STACK. ALL RIGHTS RESERVED.</p>
  </div>
</section>

<!-- Title slide A -->
<div class="slide" style="left:28px;top:742px">
  <svg class="shape" width="562" height="316" viewBox="0 0 562 316">
    <defs><linearGradient id="pA" x1="0" y1="0" x2="1" y2="1"><stop offset="0" stop-color="#a3abb3"/><stop offset=".55" stop-color="#626a73"/><stop offset="1" stop-color="#2c3036"/></linearGradient></defs>
    <path d="M238,316 C258,220 266,120 292,62 C310,18 338,0 380,0 L562,0 L562,316 Z" fill="var(--gold)"/>
    <path role="img" aria-label="Photo: two business people looking up at a modern glass building" d="M282,316 C296,230 304,150 326,90 C342,44 364,20 404,0 L562,0 L562,316 Z" fill="url(#pA)"/>
  </svg>
  <div class="brand" style="left:34px;top:40px"><span class="sq"></span><span class="name">LUMO STACK</span></div>
  <div class="title-gold" style="left:34px;top:118px">PRESENTATION</div>
  <div class="title-dark" style="left:34px;top:138px">HEADING HERE</div>
  <p class="body" style="left:34px;top:172px;width:190px">Lorem ipsum dolor sit amet, consectetur adipiscing elit. Vivamus eu dui ex. Curabitur dapibus dignissim dui, in molestie metus feugiat sed. Praesent aliquet lorem ex.</p>
  <p class="body" style="left:34px;top:226px;color:var(--ink)">Friday, July 14, 2023</p>
  <p class="tiny" style="left:34px;top:278px">COPYRIGHT © 2023 LUMO STACK. ALL RIGHTS RESERVED.</p>
</div>

<!-- Title slide B -->
<div class="slide" style="left:609px;top:742px">
  <svg class="shape" width="562" height="316" viewBox="0 0 562 316">
    <defs><linearGradient id="pB" x1="0" y1="0" x2="1" y2="1"><stop offset="0" stop-color="#7c8a99"/><stop offset=".5" stop-color="#3c4652"/><stop offset="1" stop-color="#1d2228"/></linearGradient></defs>
    <path d="M238,316 C258,220 266,120 292,62 C310,18 338,0 380,0 L562,0 L562,316 Z" fill="var(--gold)"/>
    <path role="img" aria-label="Photo: hands shaking over a tablet showing a financial chart" d="M282,316 C296,230 304,150 326,90 C342,44 364,20 404,0 L562,0 L562,316 Z" fill="url(#pB)"/>
  </svg>
  <div class="brand" style="left:34px;top:40px"><span class="sq"></span><span class="name">LUMO STACK</span></div>
  <div class="title-gold" style="left:34px;top:118px">PRESENTATION</div>
  <div class="title-dark" style="left:34px;top:138px">HEADING HERE</div>
  <p class="body" style="left:34px;top:172px;width:190px">Lorem ipsum dolor sit amet, consectetur adipiscing elit. Vivamus eu dui ex. Curabitur dapibus dignissim dui, in molestie metus feugiat sed. Praesent aliquet lorem ex.</p>
  <p class="body" style="left:34px;top:226px;color:var(--ink)">Friday, July 14, 2023</p>
  <p class="tiny" style="left:34px;top:278px">COPYRIGHT © 2023 LUMO STACK. ALL RIGHTS RESERVED.</p>
</div>

<!-- About us -->
<div class="slide" style="left:28px;top:1077px">
  <div role="img" aria-label="Photo: office building facade in grey tones" style="left:0;top:0;width:250px;height:120px;background:linear-gradient(135deg,#6a6a6a,#3d3d3d)"></div>
  <div role="img" aria-label="Photo: city buildings with warm light" style="left:250px;top:0;width:312px;height:255px;background:linear-gradient(135deg,#d9a65a,#8a5d22)"></div>
  <div style="left:250px;top:0;width:272px;height:255px;background:rgba(178,120,38,.92)"></div>
  <div class="h-display light" style="left:18px;top:18px">About Us</div>
  <div class="h-bar" style="left:18px;top:38px;background:var(--yellow)"></div>
  <p class="body w" style="left:18px;top:56px;width:220px;font-weight:700">Lorem ipsum dolor sit amet, consectetur adipiscing elit. Vivamus eu dui ex. Curabitur dapibus dignissim dui, in molestie metus feugiat sed. Praesent aliquet lorem ex, eu dapibus odio varius at. Duis eget tellus porta, consequat lacus vitae, venenatis dolor.</p>
  <p style="left:18px;top:142px;width:225px;font-size:8px;font-weight:600;color:var(--gold);line-height:1.3">Lorem ipsum dolor sit amet, consectetur adipiscing elit. Vivamus eu dui ex.</p>
  <p class="body" style="left:18px;top:182px;width:222px">Lorem ipsum dolor sit amet, consectetur adipiscing elit. Vivamus eu dui ex. Curabitur dapibus dignissim dui, in molestie metus feugiat sed. Praesent aliquet lorem ex, eu dapibus odio varius at. Duis eget tellus porta, consequat lacus vitae, venenatis dolor. Nulla facilisi.</p>
  <div style="left:270px;top:36px;font-size:10px;font-weight:600;color:#fff">Heading Goes Here</div>
  <ul class="ticks" style="left:270px;top:72px;width:236px">
    <li>Lorem ipsum dolor sit amet, consectetur adipiscing elit. Vivamus eu dui ex. Curabitur dapibus dignissim dui, in molestie metus feugiat sed.</li>
    <li>Praesent aliquet lorem ex, eu dapibus odio varius at. Duis eget tellus porta, consequat lacus vitae, venenatis dolor.</li>
    <li>Lorem ipsum dolor sit amet, consectetur adipiscing elit. Vivamus eu dui ex. Curabitur dapibus dignissim dui, in molestie metus feugiat sed.</li>
    <li>Praesent aliquet lorem ex, eu dapibus odio varius at. Duis eget tellus porta, consequat lacus vitae, venenatis dolor.</li>
  </ul>
  <div class="foot"><span class="sq"></span><span class="name">LUMO STACK</span><span class="copy">COPYRIGHT © 2023 LUMO STACK. ALL RIGHTS RESERVED.</span><span class="pg">3</span></div>
</div>

<!-- Meet our team -->
<div class="slide" style="left:609px;top:1077px">
  <div class="h-display" style="left:18px;top:18px">Meet Our Team</div>
  <div class="h-bar" style="left:18px;top:38px"></div>
  <svg class="shape" width="562" height="316" viewBox="0 0 562 316">
    <defs><linearGradient id="pT" x1="0" y1="0" x2="0" y2="1"><stop offset="0" stop-color="#eeeeee"/><stop offset="1" stop-color="#9a9a9a"/></linearGradient></defs>
    <circle role="img" aria-label="Team member portrait" cx="115" cy="124" r="47" fill="url(#pT)" stroke="var(--yellow)" stroke-width="2"/>
    <circle role="img" aria-label="Team member portrait" cx="281" cy="124" r="47" fill="url(#pT)" stroke="var(--yellow)" stroke-width="2"/>
    <circle role="img" aria-label="Team member portrait" cx="447" cy="124" r="47" fill="url(#pT)" stroke="var(--yellow)" stroke-width="2"/>
  </svg>
  <div class="sub-gold c" style="left:45px;top:185px;width:140px">Name Goes Here</div>
  <div class="sub-gold c" style="left:211px;top:185px;width:140px">Name Goes Here</div>
  <div class="sub-gold c" style="left:377px;top:185px;width:140px">Name Goes Here</div>
  <div class="body c" style="left:45px;top:197px;width:140px;color:var(--ink)">Job Title Goes Here</div>
  <div class="body c" style="left:211px;top:197px;width:140px;color:var(--ink)">Job Title Goes Here</div>
  <div class="body c" style="left:377px;top:197px;width:140px;color:var(--ink)">Job Title Goes Here</div>
  <p class="body c" style="left:45px;top:212px;width:140px">Lorem ipsum dolor sit amet, consectetur adipiscing elit. Vivamus eu dui ex. Curabitur dapibus dignissim dui, in molestie metus feugiat sed. Praesent aliquet lorem ex, eu dapibus odio varius at.</p>
  <p class="body c" style="left:211px;top:212px;width:140px">Lorem ipsum dolor sit amet, consectetur adipiscing elit. Vivamus eu dui ex. Curabitur dapibus dignissim dui, in molestie metus feugiat sed. Praesent aliquet lorem ex, eu dapibus odio varius at.</p>
  <p class="body c" style="left:377px;top:212px;width:140px">Lorem ipsum dolor sit amet, consectetur adipiscing elit. Vivamus eu dui ex. Curabitur dapibus dignissim dui, in molestie metus feugiat sed. Praesent aliquet lorem ex, eu dapibus odio varius at.</p>
  <div class="foot"><span class="sq"></span><span class="name">LUMO STACK</span><span class="copy">COPYRIGHT © 2023 LUMO STACK. ALL RIGHTS RESERVED.</span><span class="pg">4</span></div>
</div>

<!-- Heading with four photos -->
<div class="slide" style="left:28px;top:1412px">
  <div role="img" aria-label="Photo: office interior in warm gold tones" style="left:0;top:0;width:562px;height:110px;background:linear-gradient(90deg,#c08a3e,#d8a860 60%,#b27a30)"></div>
  <div class="h-display light" style="left:18px;top:18px">Heading Goes Here</div>
  <div class="h-bar" style="left:18px;top:38px;background:#fff"></div>
  <div role="img" aria-label="Photo: business handshake at a desk" style="left:32px;top:73px;width:117px;height:70px;background:linear-gradient(135deg,#8fa0b0,#3f4a55)"></div>
  <div role="img" aria-label="Photo: team reviewing documents at a table" style="left:159px;top:73px;width:117px;height:70px;background:linear-gradient(135deg,#d8c7ad,#8d7352)"></div>
  <div role="img" aria-label="Photo: hand pointing at printed charts" style="left:287px;top:73px;width:117px;height:70px;background:linear-gradient(135deg,#eef1f5,#9fb0c4)"></div>
  <div role="img" aria-label="Photo: people working with papers and laptop" style="left:415px;top:73px;width:117px;height:70px;background:linear-gradient(135deg,#6e6a66,#2f2c2a)"></div>
  <div class="sub-gold" style="left:36px;top:158px">Heading Goes Here</div>
  <div class="sub-gold" style="left:163px;top:158px">Heading Goes Here</div>
  <div class="sub-gold" style="left:291px;top:158px">Heading Goes Here</div>
  <div class="sub-gold" style="left:419px;top:158px">Heading Goes Here</div>
  <p class="body" style="left:36px;top:174px;width:112px">Lorem ipsum dolor sit amet, consectetur adipiscing elit. Vivamus eu dui ex. Curabitur dapibus dignissim dui, in molestie metus feugiat sed. Praesent aliquet lorem ex, eu dapibus odio varius at. Duis eget tellus porta, consequat lacus vitae, venenatis dolor. Nulla facilisi.</p>
  <p class="body" style="left:163px;top:174px;width:112px">Lorem ipsum dolor sit amet, consectetur adipiscing elit. Vivamus eu dui ex. Curabitur dapibus dignissim dui, in molestie metus feugiat sed. Praesent aliquet lorem ex, eu dapibus odio varius at. Duis eget tellus porta, consequat lacus vitae, venenatis dolor. Nulla facilisi.</p>
  <p class="body" style="left:291px;top:174px;width:112px">Lorem ipsum dolor sit amet, consectetur adipiscing elit. Vivamus eu dui ex. Curabitur dapibus dignissim dui, in molestie metus feugiat sed. Praesent aliquet lorem ex, eu dapibus odio varius at. Duis eget tellus porta, consequat lacus vitae, venenatis dolor. Nulla facilisi.</p>
  <p class="body" style="left:419px;top:174px;width:112px">Lorem ipsum dolor sit amet, consectetur adipiscing elit. Vivamus eu dui ex. Curabitur dapibus dignissim dui, in molestie metus feugiat sed. Praesent aliquet lorem ex, eu dapibus odio varius at. Duis eget tellus porta, consequat lacus vitae, venenatis dolor. Nulla facilisi.</p>
  <div class="foot"><span class="sq"></span><span class="name">LUMO STACK</span><span class="copy">COPYRIGHT © 2023 LUMO STACK. ALL RIGHTS RESERVED.</span><span class="pg">5</span></div>
</div>

<!-- Heading with four icons -->
<div class="slide" style="left:609px;top:1412px">
  <div class="h-display" style="left:18px;top:18px">Heading Goes Here</div>
  <div class="h-bar" style="left:18px;top:38px"></div>
  <svg class="shape" width="562" height="316" viewBox="0 0 562 316">
    <circle cx="97" cy="95" r="27" fill="var(--gold)"/>
    <circle cx="97" cy="89" r="6" fill="#fff"/><path d="M85,106 Q97,92 109,106 Z" fill="#fff"/>
    <circle cx="220" cy="95" r="27" fill="var(--yellow)"/>
    <rect x="207" y="84" width="26" height="22" rx="2" fill="none" stroke="#fff" stroke-width="2"/>
    <line x1="207" y1="90" x2="233" y2="90" stroke="#fff" stroke-width="2"/>
    <g fill="#fff"><rect x="211" y="94" width="4" height="3"/><rect x="218" y="94" width="4" height="3"/><rect x="225" y="94" width="4" height="3"/><rect x="211" y="100" width="4" height="3"/><rect x="218" y="100" width="4" height="3"/><rect x="225" y="100" width="4" height="3"/></g>
    <circle cx="342" cy="95" r="27" fill="var(--gold)"/>
    <circle cx="342" cy="95" r="14" fill="none" stroke="#fff" stroke-width="2"/>
    <path d="M342,87 V95 H349" fill="none" stroke="#fff" stroke-width="2"/>
    <circle cx="465" cy="95" r="27" fill="var(--yellow)"/>
    <path d="M453,94 h6 v14 h-6 Z M461,108 V94 l6,-11 q4,0 3,6 l-1,4 h8 q3,1 2,4 l-3,9 q-1,2 -4,2 Z" fill="#fff"/>
  </svg>
  <div class="sub-dark c" style="left:42px;top:130px;width:110px">Heading Goes Here</div>
  <div class="sub-dark c" style="left:165px;top:130px;width:110px">Heading Goes Here</div>
  <div class="sub-dark c" style="left:287px;top:130px;width:110px">Heading Goes Here</div>
  <div class="sub-dark c" style="left:410px;top:130px;width:110px">Heading Goes Here</div>
  <p class="body c" style="left:42px;top:143px;width:110px">Lorem ipsum dolor sit amet, consectetur adipiscing elit. Vivamus eu dui ex. Curabitur dapibus dignissim dui, in molestie metus feugiat sed.</p>
  <p class="body c" style="left:165px;top:143px;width:110px">Lorem ipsum dolor sit amet, consectetur adipiscing elit. Vivamus eu dui ex. Curabitur dapibus dignissim dui, in molestie metus feugiat sed.</p>
  <p class="body c" style="left:287px;top:143px;width:110px">Lorem ipsum dolor sit amet, consectetur adipiscing elit. Vivamus eu dui ex. Curabitur dapibus dignissim dui, in molestie metus feugiat sed.</p>
  <p class="body c" style="left:410px;top:143px;width:110px">Lorem ipsum dolor sit amet, consectetur adipiscing elit. Vivamus eu dui ex. Curabitur dapibus dignissim dui, in molestie metus feugiat sed.</p>
  <ul class="dots" style="left:47px;top:200px;width:100px"><li>Lorem Ipsum Dolor Sit Amet.</li><li>Consectetur Adipiscing Elit.</li><li>Vivamus Eu Dui Ex.</li><li>Curabitur Dapibus Dignissim Dui, In Molestie</li><li>Metus Feugiat Sed.</li></ul>
  <ul class="dots" style="left:170px;top:200px;width:100px"><li>Lorem Ipsum Dolor Sit Amet.</li><li>Consectetur Adipiscing Elit.</li><li>Vivamus Eu Dui Ex.</li><li>Curabitur Dapibus Dignissim Dui, In Molestie</li><li>Metus Feugiat Sed.</li></ul>
  <ul class="dots" style="left:292px;top:200px;width:100px"><li>Lorem Ipsum Dolor Sit Amet.</li><li>Consectetur Adipiscing Elit.</li><li>Vivamus Eu Dui Ex.</li><li>Curabitur Dapibus Dignissim Dui, In Molestie</li><li>Metus Feugiat Sed.</li></ul>
  <ul class="dots" style="left:415px;top:200px;width:100px"><li>Lorem Ipsum Dolor Sit Amet.</li><li>Consectetur Adipiscing Elit.</li><li>Vivamus Eu Dui Ex.</li><li>Curabitur Dapibus Dignissim Dui, In Molestie</li><li>Metus Feugiat Sed.</li></ul>
  <div class="foot"><span class="sq"></span><span class="name">LUMO STACK</span><span class="copy">COPYRIGHT © 2023 LUMO STACK. ALL RIGHTS RESERVED.</span><span class="pg">6</span></div>
</div>

<!-- Timeline -->
<div class="slide" style="left:28px;top:1747px">
  <div class="h-display" style="left:18px;top:18px">Heading Goes Here</div>
  <div class="h-bar" style="left:18px;top:38px"></div>
  <svg class="shape" width="562" height="316" viewBox="0 0 562 316">
    <line x1="0" y1="129" x2="540" y2="129" stroke="#bbb" stroke-width="1" stroke-dasharray="2 2"/>
    <path d="M536,126 L541,129 L536,132" fill="none" stroke="#bbb"/>
    <g font-family="Montserrat,sans-serif" font-size="13" font-weight="600" fill="#fff" text-anchor="middle">
      <circle cx="89" cy="129" r="13" fill="var(--gold)"/><text x="89" y="134">1</text>
      <circle cx="185" cy="129" r="13" fill="var(--yellow)"/><text x="185" y="134">2</text>
      <circle cx="281" cy="129" r="13" fill="var(--gold)"/><text x="281" y="134">3</text>
      <circle cx="377" cy="129" r="13" fill="var(--yellow)"/><text x="377" y="134">4</text>
      <circle cx="473" cy="129" r="13" fill="var(--gold)"/><text x="473" y="134">5</text>
    </g>
  </svg>
  <p class="body c" style="left:49px;top:155px;width:80px">Lorem ipsum dolor sit amet, consectetur adipiscing elit. Vivamus eu dui ex. Curabitur dapibus dignissim dui, in molestie metus feugiat sed. Praesent aliquet lorem ex.</p>
  <p class="body c" style="left:145px;top:155px;width:80px">Lorem ipsum dolor sit amet, consectetur adipiscing elit. Vivamus eu dui ex. Curabitur dapibus dignissim dui, in molestie metus feugiat sed. Praesent aliquet lorem ex.</p>
  <p class="body c" style="left:241px;top:155px;width:80px">Lorem ipsum dolor sit amet, consectetur adipiscing elit. Vivamus eu dui ex. Curabitur dapibus dignissim dui, in molestie metus feugiat sed. Praesent aliquet lorem ex.</p>
  <p class="body c" style="left:337px;top:155px;width:80px">Lorem ipsum dolor sit amet, consectetur adipiscing elit. Vivamus eu dui ex. Curabitur dapibus dignissim dui, in molestie metus feugiat sed. Praesent aliquet lorem ex.</p>
  <p class="body c" style="left:433px;top:155px;width:80px">Lorem ipsum dolor sit amet, consectetur adipiscing elit. Vivamus eu dui ex. Curabitur dapibus dignissim dui, in molestie metus feugiat sed. Praesent aliquet lorem ex.</p>
  <div class="foot"><span class="sq"></span><span class="name">LUMO STACK</span><span class="copy">COPYRIGHT © 2023 LUMO STACK. ALL RIGHTS RESERVED.</span><span class="pg">7</span></div>
</div>

<!-- Cycle wheel -->
<div class="slide" style="left:609px;top:1747px">
  <div class="h-display" style="left:18px;top:18px">Heading Goes Here</div>
  <div class="h-bar" style="left:18px;top:38px"></div>
  <svg class="shape" width="562" height="316" viewBox="0 0 562 316">
    <path d="M281,171 L281,89 A82,82 0 0 1 363,171 Z" fill="var(--yellow)"/>
    <path d="M281,171 L363,171 A82,82 0 0 1 281,253 Z" fill="var(--gold)"/>
    <path d="M281,171 L281,253 A82,82 0 0 1 199,171 Z" fill="var(--yellow)"/>
    <path d="M281,171 L199,171 A82,82 0 0 1 281,89 Z" fill="var(--gold)"/>
    <line x1="281" y1="87" x2="281" y2="255" stroke="#fff" stroke-width="3"/>
    <line x1="197" y1="171" x2="365" y2="171" stroke="#fff" stroke-width="3"/>
    <circle cx="281" cy="171" r="42" fill="#fff"/>
    <circle cx="281" cy="171" r="34" fill="none" stroke="#e6e6e6" stroke-width="5"/>
    <rect x="271" y="161" width="20" height="20" fill="var(--gold)"/>
    <circle cx="225" cy="118" r="12" fill="#fff"/><circle cx="225" cy="116" r="4.5" fill="var(--gold)"/><rect x="223" y="121" width="4" height="3" fill="var(--gold)"/>
    <circle cx="337" cy="118" r="12" fill="#fff"/><circle cx="335" cy="116" r="4.5" fill="none" stroke="var(--gold)" stroke-width="1.6"/><line x1="338" y1="119" x2="342" y2="123" stroke="var(--gold)" stroke-width="1.6"/>
    <circle cx="225" cy="224" r="12" fill="#fff"/><rect x="219" y="224" width="3" height="5" fill="var(--gold)"/><rect x="224" y="220" width="3" height="9" fill="var(--gold)"/><rect x="229" y="217" width="3" height="12" fill="var(--gold)"/>
    <circle cx="337" cy="224" r="12" fill="#fff"/><circle cx="334" cy="221" r="2.5" fill="var(--gold)"/><circle cx="340" cy="221" r="2.5" fill="var(--gold)"/><path d="M330,229 Q334,224 338,229 Z M336,229 Q340,224 344,229 Z" fill="var(--gold)"/>
  </svg>
  <div class="sub-yellow r" style="left:30px;top:86px;width:150px">Heading Goes Here</div>
  <p class="body r" style="left:30px;top:100px;width:150px">Lorem ipsum dolor sit amet, consectetur adipiscing elit. Vivamus eu dui ex. Curabitur dapibus dignissim dui, in molestie metus feugiat sed. Praesent aliquet lorem ex.</p>
  <div class="sub-gold r" style="left:30px;top:196px;width:150px">Heading Goes Here</div>
  <p class="body r" style="left:30px;top:210px;width:150px">Lorem ipsum dolor sit amet, consectetur adipiscing elit. Vivamus eu dui ex. Curabitur dapibus dignissim dui, in molestie metus feugiat sed. Praesent aliquet lorem ex.</p>
  <div class="sub-gold" style="left:378px;top:86px;width:150px">Heading Goes Here</div>
  <p class="body" style="left:378px;top:100px;width:150px">Lorem ipsum dolor sit amet, consectetur adipiscing elit. Vivamus eu dui ex. Curabitur dapibus dignissim dui, in molestie metus feugiat sed. Praesent aliquet lorem ex.</p>
  <div class="sub-yellow" style="left:378px;top:196px;width:150px">Heading Goes Here</div>
  <p class="body" style="left:378px;top:210px;width:150px">Lorem ipsum dolor sit amet, consectetur adipiscing elit. Vivamus eu dui ex. Curabitur dapibus dignissim dui, in molestie metus feugiat sed. Praesent aliquet lorem ex.</p>
  <div class="foot"><span class="sq"></span><span class="name">LUMO STACK</span><span class="copy">COPYRIGHT © 2023 LUMO STACK. ALL RIGHTS RESERVED.</span><span class="pg">8</span></div>
</div>

<!-- Pyramid -->
<div class="slide" style="left:28px;top:2082px">
  <div class="h-display" style="left:18px;top:18px">Heading Goes Here</div>
  <div class="h-bar" style="left:18px;top:38px"></div>
  <svg class="shape" width="562" height="316" viewBox="0 0 562 316">
    <path d="M282,92 L250,140 L282,150 Z" fill="var(--gold-deep)"/>
    <path d="M282,92 L314,140 L282,150 Z" fill="var(--gold)"/>
    <path d="M245,148 L282,158 L282,192 L222,176 Z" fill="#d9a93a"/>
    <path d="M319,148 L282,158 L282,192 L342,176 Z" fill="var(--yellow)"/>
    <path d="M216,184 L282,201 L282,232 L196,208 Z" fill="#222"/>
    <path d="M348,184 L282,201 L282,232 L368,208 Z" fill="var(--dark)"/>
    <line x1="180" y1="155" x2="235" y2="155" stroke="#ddd"/>
    <circle cx="182" cy="155" r="12" fill="var(--yellow)"/><rect x="176" y="151" width="12" height="8" rx="1" fill="#fff"/>
    <line x1="320" y1="115" x2="370" y2="102" stroke="#ddd"/>
    <circle cx="370" cy="102" r="12" fill="var(--gold)"/><circle cx="370" cy="100" r="4.5" fill="#fff"/><rect x="368" y="105" width="4" height="3" fill="#fff"/>
    <line x1="340" y1="200" x2="370" y2="210" stroke="#ddd"/>
    <circle cx="370" cy="210" r="12" fill="var(--dark)"/><circle cx="370" cy="210" r="5" fill="none" stroke="#fff" stroke-width="2" stroke-dasharray="2 1.5"/>
  </svg>
  <div class="sub-yellow r" style="left:38px;top:128px;width:122px">Heading Goes Here</div>
  <p class="body r" style="left:38px;top:142px;width:122px">Lorem ipsum dolor sit amet, consectetur adipiscing elit. Vivamus eu dui ex. Curabitur dapibus dignissim dui, in molestie metus feugiat sed.</p>
  <div class="sub-gold" style="left:392px;top:84px;width:130px">Heading Goes Here</div>
  <p class="body" style="left:392px;top:98px;width:130px">Lorem ipsum dolor sit amet, consectetur adipiscing elit. Vivamus eu dui ex. Curabitur dapibus dignissim dui, in molestie metus feugiat sed.</p>
  <div class="sub-dark" style="left:392px;top:192px;width:130px">Heading Goes Here</div>
  <p class="body" style="left:392px;top:206px;width:130px">Lorem ipsum dolor sit amet, consectetur adipiscing elit. Vivamus eu dui ex. Curabitur dapibus dignissim dui, in molestie metus feugiat sed.</p>
  <div class="foot"><span class="sq"></span><span class="name">LUMO STACK</span><span class="copy">COPYRIGHT © 2023 LUMO STACK. ALL RIGHTS RESERVED.</span><span class="pg">9</span></div>
</div>

<!-- Charts -->
<div class="slide" style="left:609px;top:2082px">
  <div class="h-display" style="left:18px;top:18px">Heading Goes Here</div>
  <div class="h-bar" style="left:18px;top:38px"></div>
  <svg class="shape" width="562" height="316" viewBox="0 0 562 316" font-family="Montserrat,sans-serif" font-size="5" fill="var(--ink)">
    <g stroke="#eee">
      <line x1="86" y1="78" x2="86" y2="180"/><line x1="112" y1="78" x2="112" y2="180"/><line x1="138" y1="78" x2="138" y2="180"/><line x1="164" y1="78" x2="164" y2="180"/><line x1="190" y1="78" x2="190" y2="180"/><line x1="216" y1="78" x2="216" y2="180"/><line x1="242" y1="78" x2="242" y2="180"/><line x1="268" y1="78" x2="268" y2="180"/>
    </g>
    <rect x="86" y="86" width="49" height="7" fill="var(--gold)"/><rect x="135" y="86" width="38" height="7" fill="var(--yellow)"/><rect x="173" y="86" width="62" height="7" fill="var(--dark)"/>
    <rect x="86" y="108" width="45" height="7" fill="var(--gold)"/><rect x="131" y="108" width="22" height="7" fill="var(--yellow)"/><rect x="153" y="108" width="35" height="7" fill="var(--dark)"/>
    <rect x="86" y="131" width="40" height="7" fill="var(--gold)"/><rect x="126" y="131" width="26" height="7" fill="var(--yellow)"/><rect x="152" y="131" width="42" height="7" fill="var(--dark)"/>
    <rect x="86" y="154" width="45" height="7" fill="var(--gold)"/><rect x="131" y="154" width="35" height="7" fill="var(--yellow)"/><rect x="166" y="154" width="24" height="7" fill="var(--dark)"/>
    <text x="48" y="91">Category 4</text><text x="48" y="113">Category 3</text><text x="48" y="136">Category 2</text><text x="48" y="159">Category 1</text>
    <g text-anchor="middle"><text x="86" y="188">0</text><text x="112" y="188">2</text><text x="138" y="188">4</text><text x="164" y="188">6</text><text x="190" y="188">8</text><text x="216" y="188">10</text><text x="242" y="188">12</text><text x="268" y="188">14</text></g>
    <g stroke="#eee"><line x1="300" y1="78" x2="525" y2="78"/><line x1="300" y1="98" x2="525" y2="98"/><line x1="300" y1="118" x2="525" y2="118"/><line x1="300" y1="138" x2="525" y2="138"/><line x1="300" y1="158" x2="525" y2="158"/><line x1="300" y1="178" x2="525" y2="178"/></g>
    <g text-anchor="end"><text x="295" y="80">10</text><text x="295" y="100">8</text><text x="295" y="120">6</text><text x="295" y="140">4</text><text x="295" y="160">2</text><text x="295" y="180">0</text></g>
    <rect x="317" y="98" width="10" height="80" fill="var(--gold)"/><rect x="328" y="124" width="10" height="54" fill="var(--yellow)"/><rect x="339" y="160" width="10" height="18" fill="var(--dark)"/>
    <rect x="370" y="114" width="10" height="64" fill="var(--gold)"/><rect x="381" y="130" width="10" height="48" fill="var(--yellow)"/><rect x="392" y="160" width="10" height="18" fill="var(--dark)"/>
    <rect x="423" y="126" width="10" height="52" fill="var(--gold)"/><rect x="434" y="94" width="10" height="84" fill="var(--yellow)"/><rect x="445" y="150" width="10" height="28" fill="var(--dark)"/>
    <rect x="476" y="142" width="10" height="36" fill="var(--gold)"/><rect x="487" y="160" width="10" height="18" fill="var(--yellow)"/><rect x="498" y="134" width="10" height="44" fill="var(--dark)"/>
    <g text-anchor="middle"><text x="333" y="188">Category 1</text><text x="386" y="188">Category 2</text><text x="439" y="188">Category 3</text><text x="492" y="188">Category 4</text></g>
  </svg>
  <div class="sub-gold" style="left:45px;top:208px">Heading Goes Here</div>
  <p class="body" style="left:45px;top:222px;width:225px">Lorem ipsum dolor sit amet, consectetur adipiscing elit. Vivamus eu dui ex. Curabitur dapibus dignissim dui, in molestie metus feugiat sed. Praesent aliquet lorem ex.</p>
  <div class="sub-gold" style="left:295px;top:208px">Heading Goes Here</div>
  <p class="body" style="left:295px;top:222px;width:225px">Lorem ipsum dolor sit amet, consectetur adipiscing elit. Vivamus eu dui ex. Curabitur dapibus dignissim dui, in molestie metus feugiat sed. Praesent aliquet lorem ex.</p>
  <div class="foot"><span class="sq"></span><span class="name">LUMO STACK</span><span class="copy">COPYRIGHT © 2023 LUMO STACK. ALL RIGHTS RESERVED.</span><span class="pg">10</span></div>
</div>

<!-- Donuts -->
<div class="slide" style="left:28px;top:2417px">
  <div class="h-display" style="left:18px;top:18px">Heading Goes Here</div>
  <div class="h-bar" style="left:18px;top:38px"></div>
  <svg class="shape" width="562" height="316" viewBox="0 0 562 316">
    <circle cx="125" cy="138" r="50" fill="none" stroke="#e0e0e0" stroke-width="12"/>
    <circle cx="125" cy="138" r="50" fill="none" stroke="var(--gold)" stroke-width="12" stroke-dasharray="110 314" transform="rotate(-90 125 138)"/>
    <circle cx="281" cy="138" r="50" fill="none" stroke="#e0e0e0" stroke-width="12"/>
    <circle cx="281" cy="138" r="50" fill="none" stroke="var(--yellow)" stroke-width="12" stroke-dasharray="204 314" transform="rotate(-90 281 138)"/>
    <circle cx="437" cy="138" r="50" fill="none" stroke="#e0e0e0" stroke-width="12"/>
    <circle cx="437" cy="138" r="50" fill="none" stroke="var(--dark)" stroke-width="12" stroke-dasharray="267 314" transform="rotate(-90 437 138)"/>
  </svg>
  <div class="pct c" style="left:75px;top:126px;width:100px;color:var(--gold)">35%</div>
  <div class="pct c" style="left:231px;top:126px;width:100px;color:var(--yellow)">65%</div>
  <div class="pct c" style="left:387px;top:126px;width:100px;color:var(--dark)">85%</div>
  <div class="sub-dark c" style="left:60px;top:204px;width:130px">Heading Goes Here</div>
  <div class="sub-yellow c" style="left:216px;top:204px;width:130px">Heading Goes Here</div>
  <div class="sub-dark c" style="left:372px;top:204px;width:130px">Heading Goes Here</div>
  <p class="body c" style="left:60px;top:219px;width:130px">Lorem ipsum dolor sit amet, consectetur adipiscing elit. Vivamus eu dui ex. Curabitur dapibus dignissim dui, in molestie metus feugiat sed.</p>
  <p class="body c" style="left:216px;top:219px;width:130px">Lorem ipsum dolor sit amet, consectetur adipiscing elit. Vivamus eu dui ex. Curabitur dapibus dignissim dui, in molestie metus feugiat sed.</p>
  <p class="body c" style="left:372px;top:219px;width:130px">Lorem ipsum dolor sit amet, consectetur adipiscing elit. Vivamus eu dui ex. Curabitur dapibus dignissim dui, in molestie metus feugiat sed.</p>
  <div class="foot"><span class="sq"></span><span class="name">LUMO STACK</span><span class="copy">COPYRIGHT © 2023 LUMO STACK. ALL RIGHTS RESERVED.</span><span class="pg">11</span></div>
</div>

<!-- Table -->
<div class="slide" style="left:609px;top:2417px">
  <div class="h-display" style="left:18px;top:18px">Heading Goes Here</div>
  <div class="h-bar" style="left:18px;top:38px"></div>
  <table class="data-table" style="left:29px;top:72px">
    <thead><tr><th class="lead">Heading Goes Here</th><th class="col">Heading<br>Goes Here</th><th class="col">Heading<br>Goes Here</th><th class="col">Heading<br>Goes Here</th><th class="col">Heading<br>Goes Here</th></tr></thead>
    <tbody>
      <tr><td class="lead">Lorem ipsum dolor sit amet</td><td class="hl">23</td><td>12</td><td>78</td><td>78</td></tr>
      <tr><td class="lead">Vivamus eu dui ex. Curabitur dapibus</td><td class="hl">45</td><td>56</td><td>12</td><td>76</td></tr>
      <tr><td class="lead">Praesent aliquet lorem ex, eu dapibus</td><td class="hl">78</td><td>76</td><td>34</td><td>34</td></tr>
      <tr><td class="lead">Duis eget tellus porta, consequat lacus</td><td class="hl">22</td><td>12</td><td>55</td><td>67</td></tr>
      <tr><td class="lead">Donec risus orci, gravida sit amet</td><td class="hl">34</td><td>66</td><td>45</td><td>11</td></tr>
      <tr><td class="lead">Nunc placerat, arcu nec mattis</td><td class="hl">67</td><td>47</td><td>78</td><td>23</td></tr>
      <tr><td class="lead">Nam semper tristique mauris</td><td class="hl">87</td><td>67</td><td>12</td><td>45</td></tr>
    </tbody>
  </table>
  <div class="col-frame" style="left:183px;top:68px;width:89px;height:184px"></div>
  <div class="foot"><span class="sq"></span><span class="name">LUMO STACK</span><span class="copy">COPYRIGHT © 2023 LUMO STACK. ALL RIGHTS RESERVED.</span><span class="pg">12</span></div>
</div>

<!-- Contact A -->
<div class="slide" style="left:28px;top:2752px">
  <svg class="shape" width="562" height="316" viewBox="0 0 562 316">
    <defs><linearGradient id="pC" x1="0" y1="0" x2="1" y2="1"><stop offset="0" stop-color="#6f8a8c"/><stop offset=".5" stop-color="#2f4446"/><stop offset="1" stop-color="#16211f"/></linearGradient></defs>
    <path d="M238,316 C258,220 266,120 292,62 C310,18 338,0 380,0 L562,0 L562,316 Z" fill="var(--gold)"/>
    <path role="img" aria-label="Photo: glass office tower seen from below" d="M282,316 C296,230 304,150 326,90 C342,44 364,20 404,0 L562,0 L562,316 Z" fill="url(#pC)"/>
  </svg>
  <div class="brand" style="left:34px;top:128px"><span class="sq"></span><span class="name">LUMO STACK</span></div>
  <div class="contact-head" style="left:34px;top:180px">Contact Us</div>
  <div style="left:34px;top:204px">
    <div class="contact-row"><svg viewBox="0 0 10 10"><path d="M2,1 L4,1 L5,3 L4,4 Q5,6 6,6 L7,5 L9,6 L9,8 Q5,9 1,3 Z" fill="var(--gold)"/></svg>Phone Number Goes Here</div>
    <div class="contact-row"><svg viewBox="0 0 10 10"><circle cx="5" cy="5" r="4" fill="none" stroke="var(--gold)" stroke-width="1.2"/><circle cx="5" cy="5" r="1.6" fill="none" stroke="var(--gold)" stroke-width="1.2"/></svg>E-Mail Address Goes Here</div>
    <div class="contact-row"><svg viewBox="0 0 10 10"><circle cx="5" cy="5" r="4" fill="none" stroke="var(--gold)" stroke-width="1"/><ellipse cx="5" cy="5" rx="1.8" ry="4" fill="none" stroke="var(--gold)" stroke-width="1"/><line x1="1" y1="5" x2="9" y2="5" stroke="var(--gold)" stroke-width="1"/></svg>URL Address Goes Here</div>
  </div>
  <p class="tiny" style="left:34px;top:282px">COPYRIGHT © 2023 LUMO STACK. ALL RIGHTS RESERVED.</p>
</div>

<!-- Contact B -->
<div class="slide" style="left:609px;top:2752px">
  <svg class="shape" width="562" height="316" viewBox="0 0 562 316">
    <defs><linearGradient id="pD" x1="0" y1="0" x2="1" y2="1"><stop offset="0" stop-color="#8fa2b8"/><stop offset=".5" stop-color="#3d4a5c"/><stop offset="1" stop-color="#1c232d"/></linearGradient></defs>
    <path d="M238,316 C258,220 266,120 292,62 C310,18 338,0 380,0 L562,0 L562,316 Z" fill="var(--gold)"/>
    <path role="img" aria-label="Photo: business handshake in a bright office" d="M282,316 C296,230 304,150 326,90 C342,44 364,20 404,0 L562,0 L562,316 Z" fill="url(#pD)"/>
  </svg>
  <div class="brand" style="left:34px;top:128px"><span class="sq"></span><span class="name">LUMO STACK</span></div>
  <div class="contact-head" style="left:34px;top:180px">Contact Us</div>
  <div style="left:34px;top:204px">
    <div class="contact-row"><svg viewBox="0 0 10 10"><path d="M2,1 L4,1 L5,3 L4,4 Q5,6 6,6 L7,5 L9,6 L9,8 Q5,9 1,3 Z" fill="var(--gold)"/></svg>Phone Number Goes Here</div>
    <div class="contact-row"><svg viewBox="0 0 10 10"><circle cx="5" cy="5" r="4" fill="none" stroke="var(--gold)" stroke-width="1.2"/><circle cx="5" cy="5" r="1.6" fill="none" stroke="var(--gold)" stroke-width="1.2"/></svg>E-Mail Address Goes Here</div>
    <div class="contact-row"><svg viewBox="0 0 10 10"><circle cx="5" cy="5" r="4" fill="none" stroke="var(--gold)" stroke-width="1"/><ellipse cx="5" cy="5" rx="1.8" ry="4" fill="none" stroke="var(--gold)" stroke-width="1"/><line x1="1" y1="5" x2="9" y2="5" stroke="var(--gold)" stroke-width="1"/></svg>URL Address Goes Here</div>
  </div>
  <p class="tiny" style="left:34px;top:282px">COPYRIGHT © 2023 LUMO STACK. ALL RIGHTS RESERVED.</p>
</div>

</body>
</html>
```